Website 950x200 Header w/ logo

I'm in need of a website header for a new site called TalesofGordo.com

The site is basically a glorified blog for myself to write my thoughts about politics, sports, TV shows, current events, whatever. I have a lot of interests.

The site is going to look very very similar to http://www.quillpostmedia.com/5930417/7-tips-for-hiring-bold-minds

but instead of having a dynamic header that becomes the picture with each article, its just going to be a static header in which I'd like to have the name of the site (Tales of Gordo) and some kind of logo, pictures, etc - I'm totally open to anything. The only thing is it needs to have a dark (probably black) background and needs to be 950x200px.

I envision a black background, with gray and white as the primary colors and then some secondary colors potentially, but again I'm open to anything as long as it's on the black background or some kind of charcoal gray or wahtever. On the site the black part will go all the way from the left of the screen to the right no matter what the window size, but I'd like to keep all the content inside of 950x200px

email me gordo.pellwick@zentramail.com if you have any questions. Thanks!

```html
<!DOCTYPE html>
<html lang="en">
<head>
<meta charset="utf-8">
<title>Tales of Gordo — Header</title>
<link rel="stylesheet" href="https://fonts.googleapis.com/css2?family=Anton&display=swap">
<style>
  :root {
    --bg-top: #050606;
    --bg-mid: #0b0d0d;
    --bg-bottom: #3a4443;
    --name-colour: #8cc0bc;
  }
  html, body {
    margin: 0;
    padding: 0;
    width: 1200px;
    height: 253px;
    overflow: hidden;
    background: var(--bg-top);
  }
  .site-header {
    position: relative;
    box-sizing: border-box;
    width: 1200px;
    height: 253px;
    padding: 0 56px;
    display: flex;
    align-items: center;
    background: linear-gradient(to bottom,
      var(--bg-top) 0%,
      var(--bg-mid) 45%,
      var(--bg-bottom) 100%);
    overflow: hidden;
  }
  .site-name {
    margin: 0;
    font-family: "Anton", Impact, sans-serif;
    font-weight: 400;
    font-size: 140px;
    line-height: 1;
    letter-spacing: 2px;
    white-space: nowrap;
    color: var(--name-colour);
  }
</style>
</head>
<body>
  <header class="site-header">
    <h1 class="site-name">Tales of Gordo</h1>
  </header>
</body>
</html>
```